Brackenford Medical Center Wall Mural

I need to design a wall mural for an interior wall measuring 3 meters by 20 meters. that includes either all of the services provided or a map of the locations listed on this webpage https://www.brackenford-medical.example/locations. It just needs to be very creative.

```html
<!DOCTYPE html>
<html lang="en">
<head>
<meta charset="UTF-8">
<title>Brackenford Medical Center — Services Mural</title>
<link href="https://fonts.googleapis.com/css2?family=Poppins:wght@400&display=swap" rel="stylesheet">
<style>
  :root {
    --ink: #1b1a1b;
    --crimson: #c8152f;
    --crimson-deep: #6e1822;
    --wine: #4a141b;
    --white: #ffffff;
  }
  html, body {
    margin: 0;
    padding: 0;
    width: 1200px;
    height: 180px;
    overflow: hidden;
  }
  .mural {
    position: relative;
    width: 1200px;
    height: 180px;
    background: linear-gradient(180deg, var(--ink) 0%, #3a171b 30%, #8a1826 65%, var(--crimson) 92%);
    font-family: "Poppins", sans-serif;
  }
  .service-grid {
    position: absolute;
    left: 7px;
    top: 16px;
    width: 1193px;
    display: grid;
    grid-template-columns: 168px 183px 155px 162px 182px 167px 176px;
    grid-template-rows: repeat(4, 31px);
    row-gap: 8px;
  }
  .service {
    display: flex;
    align-items: center;
    color: var(--white);
    font-size: 12.7px;
    font-weight: 400;
    white-space: nowrap;
    overflow: hidden;
  }
  .service:nth-child(7n+1) { padding-left: 20px; }
  .service:nth-child(7n+2) { padding-left: 21px; }
  .service:nth-child(7n+3) { padding-left: 24px; }
  .service:nth-child(7n+4) { padding-left: 24px; }
  .service:nth-child(7n+5) { padding-left: 24px; }
  .service:nth-child(7n+6) { padding-left: 8px; }
  .service:nth-child(7n+7) { padding-left: 19px; }
  .service--red {
    background: linear-gradient(90deg, var(--crimson) 0%, var(--crimson) 58%, var(--crimson-deep) 100%);
  }
  .service--dark {
    background: linear-gradient(90deg, var(--ink) 0%, var(--ink) 62%, var(--wine) 100%);
  }
</style>
</head>
<body>
<main class="mural" aria-label="Brackenford Medical Center services">
  <div class="service-grid">
    <div class="service service--red">Cardiac Rehab</div>
    <div class="service service--dark">Dermatology</div>
    <div class="service service--red">Endoscopy</div>
    <div class="service service--dark">General Surgery</div>
    <div class="service service--red">Laboratory Services</div>
    <div class="service service--dark">Nursing Services</div>
    <div class="service service--red">Ophthalmology</div>

    <div class="service service--dark">Cardiovascular</div>
    <div class="service service--red">Diabetes Care Services</div>
    <div class="service service--dark">Family Medicine</div>
    <div class="service service--red">Internal Medicine</div>
    <div class="service service--dark">Medical Care Unit</div>
    <div class="service service--red">Nutrition</div>
    <div class="service service--dark">Orthopedic Care</div>

    <div class="service service--red">Care Management</div>
    <div class="service service--dark">Emergency Care</div>
    <div class="service service--red">Fitness Center</div>
    <div class="service service--dark">Joint Replacement</div>
    <div class="service service--red">Medical Supplies</div>
    <div class="service service--dark">Obstetrics/Gynecology</div>
    <div class="service service--red">Otolaryngology (ENT)</div>

    <div class="service service--dark">Critical Care Unit</div>
    <div class="service service--red">Endocrinology</div>
    <div class="service service--dark">Gastroenterology</div>
    <div class="service service--red">Labor &amp; Delivery</div>
    <div class="service service--dark">Neurology</div>
    <div class="service service--red">Occupational Medicine</div>
    <div class="service service--dark">And More</div>
  </div>
</main>
</body>
</html>
```